Flyer-Design für Großhändler/Onlineshop
Zielgruppe
Velorin ist ein Großhändler für Geschäftskunden. Wir liefern Artikel der Sparten Elektronik, Bürobedarf & Verpackung über unseren Business to Business-Webshop www.velorin-beispiel.de. Der Flyer richtet sich an Firmen aus der Region mit Bedarfen in den oben genannten Produktbereichen.
Aufgabenstellung
Wir benötigen einen Zickzack-Falz Flyer 6-seitig mit den Maßen 99x210mm pro Seite, passend für DIN-Lang Briefe. Des weiteren soll unser Logo auf der Startseite oben angebraucht werden. Als Farben sollen vor allem Orange, Schwarz und Weiß verwendet werden. Zusätzlich soll es für jeden Produktbereich eine Seite des Flyers geben. Soll bedeuten: Seite 1 (Normale Startseite) Seite 2 (Elektronik) Seite 3 (Bürobedarf) Seite 4 (Verpackung) Seite 5 (Onlineshop) Seite 6 (Unternehmen und Abbildung Standort wie Ortsplan Pro, unten Impressum).
Wir treten als Vertriebspartner namhafter Hersteller auf.
Binden Sie unbedingt unsere Hersteller-Logos ein.
Alle Texte finden Sie im Dateiupload.
Gerne können Sie auch Fotos unserer Webseite nehmen.
Webshop:
www.velorin-beispiel.de
Facebook:
www.sozialnetz-beispiel.de/velorin

```html
<!DOCTYPE html>
<html lang="de">
<head>
<meta charset="utf-8">
<title>Velorin Flyer – Innenseiten</title>
<link href="https://fonts.googleapis.com/css2?family=Bitter:wght@400;700&display=swap" rel="stylesheet">
<style>
  :root{
    --orange:#ef8a2a;
    --orange-deep:#de6c12;
    --orange-light:#f9c594;
    --ink:#1c1c1c;
    --rule:#9a9a9a;
    --paper:#ffffff;
    --map:#e9e6df;
  }
  *{margin:0;padding:0;box-sizing:border-box}
  html,body{width:1200px;height:848px;overflow:hidden;background:var(--paper)}
  .sheet{position:relative;width:1200px;height:848px;font-family:"Bitter",Georgia,serif;color:var(--ink);overflow:hidden}
  .waves{position:absolute;left:0;top:0;width:1200px;height:848px}
  .divider{position:absolute;top:0;width:1px;height:848px;background:var(--rule);opacity:.8}
  .panel{position:absolute;top:0;width:400px;height:848px}
  .panel h2{position:absolute;top:42px;font-size:22px;font-weight:700;color:var(--orange)}
  .text{position:absolute;font-size:13.5px;line-height:21.5px;letter-spacing:.2px}
  .text p{margin-bottom:21.5px}
  .hl{color:var(--orange)}
  .label{position:absolute;font-size:13.5px;color:var(--orange)}
  .badge{position:absolute;left:216px;top:266px;width:118px;height:118px}
  .badge-text{position:absolute;left:216px;top:282px;width:118px;text-align:center;color:#fff;font-size:12.5px;line-height:17px;transform:rotate(9deg)}
  .brand{position:absolute;font-size:17px;font-weight:700;color:var(--ink);display:flex;align-items:center;gap:6px}
  .brand i{display:inline-block;width:10px;height:10px;background:var(--orange)}
  .shop-box{position:absolute;left:32px;top:166px;width:335px;height:412px;border-radius:8px;background:linear-gradient(135deg,#f08a2c,#dd6a12);color:#fff;padding:14px 20px 0 32px}
  .shop-box ul{list-style:none}
  .shop-box li{position:relative;font-size:19.5px;line-height:24.5px;margin-bottom:7px}
  .shop-box li::before{content:"·";position:absolute;left:-17px;top:0;font-size:16px}
  .map{position:absolute;left:28px;top:315px;width:343px;height:250px;background:linear-gradient(160deg,#ecebe4,#e2ddd2)}
</style>
</head>
<body>
<div class="sheet">
  <svg class="waves" viewBox="0 0 1200 848" aria-hidden="true">
    <defs>
      <linearGradient id="waveGrad" x1="0" y1="0" x2="1" y2="0">
        <stop offset="0" stop-color="#f08a2c"/>
        <stop offset="1" stop-color="#dc6a10"/>
      </linearGradient>
    </defs>
    <path d="M0,556 C260,690 620,800 1200,780 L1200,848 L0,848Z" fill="var(--orange-light)"/>
    <path d="M0,592 C280,735 660,830 1200,800 L1200,848 L0,848Z" fill="url(#waveGrad)"/>
  </svg>

  <div class="divider" style="left:400px"></div>
  <div class="divider" style="left:800px"></div>

  <section class="panel" style="left:0">
    <h2 style="left:33px">Verpackung</h2>
    <div class="text" style="left:33px;top:92px;width:345px">
      <p>Unter den Begriff Verpackung fallen eine <span class="hl">Vielzahl von Produkten.</span></p>
      <p>Vor allem für Industrie und Handel ist dieses eine Produktsparte mit vielen Berührungspunkten.</p>
      <p>Mittels des Velorin Fuhrparks liefern wir selbst <span class="hl">größere Mengen</span> im Umkreis von 50&#8239;km termingerecht an.</p>
    </div>
    <svg class="badge" viewBox="0 0 100 100" aria-hidden="true">
      <polygon fill="var(--orange)" points="50,0 57,6 66,3 70,11 80,10 81,19 90,21 88,30 96,35 91,42 98,50 91,58 96,65 88,70 90,79 81,81 80,90 70,89 66,97 57,94 50,100 43,94 34,97 30,89 20,90 19,81 10,79 12,70 4,65 9,58 2,50 9,42 4,35 12,30 10,21 19,19 20,10 30,11 34,3 43,6"/>
    </svg>
    <div class="badge-text">Fordern<br>Sie jetzt<br>unsere Service-<br>Informationen<br>an.</div>
    <div class="label" style="left:35px;top:424px">Unsere Verpackungs-Marken:</div>
    <div class="brand" style="left:37px;top:456px"><i></i>Kartona</div>
    <div class="brand" style="left:153px;top:456px"><i></i>Polstra</div>
    <div class="brand" style="left:257px;top:456px"><i></i>Klebwerk</div>
    <div class="brand" style="left:37px;top:510px"><i></i>Falto</div>
  </section>

  <section class="panel" style="left:400px">
    <h2 style="left:33px">Onlineshop</h2>
    <div class="text" style="left:33px;top:92px;width:345px;font-weight:700">
      Entdecken Sie unseren <span class="hl">hochmodernen</span><br>BtoB-Webshop:
    </div>
    <div class="shop-box">
      <ul>
        <li>Originalprodukte führender Hersteller</li>
        <li>Hohe Lagerverfügbarkeit für eilige Bedarfe</li>
        <li>24/7 Verfügbarkeit</li>
        <li>Integriertes Ampelsystem</li>
        <li>Individuelle Nettopreise</li>
        <li>Ansprechende Staffelpreis-<br>struktur</li>
        <li>Suche über Bestelltext &amp; Herstellerteilenummer</li>
        <li>Sofortige Bestellbestätigung per Mail</li>
      </ul>
    </div>
  </section>

  <section class="panel" style="left:800px">
    <h2 style="left:28px">Unternehmen</h2>
    <div class="text" style="left:28px;top:92px;width:360px">
      <p>Velorin ist Ihr Partner für Elektronik,<br>Bürobedarf und Verpackung der Region.</p>
      <p>Als ortsansässiger Großhändler arbeiten wir mit marktführenden Herstellern zusammen.</p>
      <p>Seit der Gründung in 2014 bieten wir Produkt und Service im Einklang für Geschäftskunden.</p>
    </div>
    <div class="label" style="left:28px;top:285px">Standort</div>
    <div class="map" role="img" aria-label="Ortsplan Pro Kartenausschnitt mit Standortmarkierung von Velorin"></div>
    <div class="label" style="left:28px;top:584px">Impressum:</div>
    <div class="text" style="left:28px;top:605px;width:360px">
      <p>Velorin<br>Jonas Ehrhardt<br>Lindenweg 12<br>12345 Musterstadt</p>
      <p>Telefon: 01234-567890<br>Fax: 01234-567891<br>E-Mail: info@velorin-beispiel.de</p>
    </div>
  </section>
</div>
</body>
</html>
```